Executive recruiting firm in need of business card design

Executive recruiting firm looking for a sleek, classy and modern business card design; card itself will be square shape, rounded edges and soft touch paper, our colors are dark blues in the navy color scale, silvers and grays. Reference our website for a better idea of our company's feel and goals at Staffbrook.com - our company message is "Employee Engagement Begins at Recruitment" this should be on the card

Industry/Entity Type

Business

```html
<!DOCTYPE html>
<html lang="en">
<head>
<meta charset="utf-8">
<title>Staffbrook — Square Business Card</title>
<link rel="stylesheet" href="https://fonts.googleapis.com/css2?family=Inter:wght@300;400;700&display=swap">
<style>
  :root {
    --navy: #1e1f45;
    --white: #ffffff;
    --backdrop: #f1f1f3;
    --ink: #1e1f45;
    --card-size: 420px;
    --radius: 26px;
  }
  * { box-sizing: border-box; margin: 0; padding: 0; }
  html, body {
    width: 1200px;
    height: 1000px;
    overflow: hidden;
    background: var(--backdrop);
    font-family: "Inter", Arial, sans-serif;
  }
  .canvas {
    position: relative;
    width: 1200px;
    height: 1000px;
  }
  .card {
    position: absolute;
    top: 290px;
    width: var(--card-size);
    height: var(--card-size);
    border-radius: var(--radius);
    overflow: hidden;
  }
  .card--front { left: 150px; background: var(--navy); }
  .card--back {
    left: 630px;
    background: var(--white);
    box-shadow: 0 1px 4px rgba(0, 0, 0, 0.12);
  }

  .brand {
    position: absolute;
    text-align: right;
  }
  .brand__name {
    display: block;
    font-weight: 300;
    font-size: 38px;
    line-height: 1;
    letter-spacing: 1px;
  }
  .brand__tagline {
    display: block;
    margin-top: 8px;
    font-weight: 300;
    font-size: 10px;
    letter-spacing: 0.6px;
  }
  .card--front .brand { right: 40px; bottom: 82px; color: var(--white); }
  .card--back .brand { right: 40px; top: 92px; color: var(--ink); }

  .holder {
    position: absolute;
    top: 178px;
    left: 0;
    width: 100%;
    text-align: center;
    color: var(--ink);
    font-size: 23px;
    line-height: 1.05;
    letter-spacing: -0.3px;
  }
  .holder__name { font-weight: 300; }
  .holder__name strong { font-weight: 700; }
  .holder__title { font-weight: 300; }

  .contact-band {
    position: absolute;
    inset: 0;
    width: 100%;
    height: 100%;
  }
  .contact-list {
    position: absolute;
    top: 282px;
    left: 66px;
    list-style: none;
    color: var(--white);
    font-size: 17px;
    font-weight: 300;
  }
  .contact-list li {
    display: flex;
    align-items: center;
    gap: 12px;
    height: 28px;
  }
  .contact-list svg {
    width: 19px;
    height: 19px;
    fill: none;
    stroke: var(--white);
    stroke-width: 1.4;
    stroke-linejoin: round;
    stroke-linecap: round;
  }
</style>
</head>
<body>
<main class="canvas">

  <section class="card card--front" aria-label="Card front">
    <div class="brand">
      <span class="brand__name">Staffbrook</span>
      <span class="brand__tagline">Employee Engagement Begins at Recruitment</span>
    </div>
  </section>

  <section class="card card--back" aria-label="Card back">
    <svg class="contact-band" viewBox="0 0 420 420" aria-hidden="true">
      <path d="M0 326 C 50 250 260 200 340 420 L 0 420 Z" fill="var(--navy)"/>
    </svg>

    <div class="brand">
      <span class="brand__name">Staffbrook</span>
      <span class="brand__tagline">Employee Engagement Begins at Recruitment</span>
    </div>

    <div class="holder">
      <p class="holder__name">Loresum <strong>ipsum</strong></p>
      <p class="holder__title">Président</p>
    </div>

    <ul class="contact-list">
      <li>
        <svg viewBox="0 0 20 20"><circle cx="10" cy="10" r="8.5"/><path d="M7 5.5l1.5 0 .8 2.2-1 .9a6 6 0 0 0 3 3l.9-1 2.2.8v1.5c-.4.6-1.2.9-2 .7A8 8 0 0 1 6.3 7.5c-.2-.8.1-1.6.7-2z"/></svg>
        <span>(418)-555-0147</span>
      </li>
      <li>
        <svg viewBox="0 0 20 20"><path d="M2 10l8-7 8 7M4.5 8v9h4v-5h3v5h4V8"/></svg>
        <span>www.staffbrook.com</span>
      </li>
      <li>
        <svg viewBox="0 0 20 20"><rect x="2" y="4" width="16" height="12"/><path d="M2 4l8 7 8-7M2 16l6-6M18 16l-6-6"/></svg>
        <span>hello@staffbrook.com</span>
      </li>
    </ul>
  </section>

</main>
</body>
</html>
```